2021 Summer Ads Whitmore Ash Custom Homes

We need a re-design of our summer ad run for our customer, Whitmore Ash Custom Homes. They are custom home builders in the mostly rural parts of West Virginia, USA. They are known for their "Forever Home" tagline. We'd like two designed ads with the main difference being just the custom home that's featured. These designs should be for a Google banner like 300 x 250 and square ad like 250 x 250. For inspiration please visit the Whitmore Ash Custom Homes website at www dot whitmoreashcustomhomes dot com

Target Market(s)

consumers / new home shoppers

Industry/Entity Type

Consumer

Requirements
Must have
• WACH logo
Price Lock Available!
Custom home pic
Learn more >
small QVTG logo mark

```html
<!DOCTYPE html>
<html lang="en">
<head>
<meta charset="utf-8">
<title>Whitmore Ash Custom Homes – Summer Ads</title>
<link href="https://fonts.googleapis.com/css2?family=Montserrat:wght@500;600;700&display=swap" rel="stylesheet">
<style>
  :root {
    --red: #e8141b;
    --charcoal: #3b3e43;
    --ink: #2e2e2e;
    --white: #ffffff;
    --page: #ffffff;
    --badge: #e9eef7;
    --badge-edge: #2a4f9b;
  }
  * { margin: 0; padding: 0; box-sizing: border-box; }
  html, body { width: 1000px; height: 1200px; overflow: hidden; background: var(--page); }
  body { position: relative; font-family: "Montserrat", Arial, sans-serif; }

  /* Banner ad */
  .banner-ad { position: absolute; left: 100px; top: 56px; width: 800px; height: 534px; overflow: hidden; }
  .banner-ad .home-photo {
    position: absolute; inset: 0;
    background: linear-gradient(180deg, #2c4f86 0%, #6f9ac2 30%, #d9dde0 50%, #8c9a7e 72%, #3f6b2e 100%);
  }
  .banner-ad .panel { position: absolute; inset: 0; width: 100%; height: 100%; }
  .banner-ad .brand-name {
    position: absolute; left: 180px; top: 150px; width: 220px; text-align: center;
    font-weight: 700; font-size: 24px; letter-spacing: 1px; color: var(--ink);
  }
  .banner-ad .tagline {
    position: absolute; left: 76px; top: 188px;
    font-weight: 600; font-size: 36px; color: var(--ink); letter-spacing: -0.5px;
  }
  .banner-ad .offer {
    position: absolute; left: 100px; top: 288px;
    font-weight: 600; font-size: 30px; line-height: 36px; color: var(--white);
  }
  .banner-ad .cta {
    position: absolute; left: 78px; top: 428px;
    display: flex; align-items: center; gap: 22px;
    font-weight: 500; font-size: 29px; color: var(--ink);
  }
  .cta-icon { width: 34px; height: 34px; }
  .partner-badge { position: absolute; width: 80px; height: 56px; background: var(--badge); border: 3px solid var(--badge-edge); }
  .banner-ad .partner-badge { left: 660px; top: 454px; }

  /* Square ad */
  .square-ad { position: absolute; left: 250px; top: 644px; width: 500px; height: 500px; overflow: hidden; }
  .square-ad .home-photo {
    position: absolute; inset: 0;
    background: linear-gradient(180deg, #3f6a2c 0%, #5f8a44 45%, #c7b9a4 70%, #a94a3c 82%, #8a8684 100%);
  }
  .square-ad .bands { position: absolute; inset: 0; width: 100%; height: 100%; }
  .square-ad .brand-name {
    position: absolute; left: 0; right: 0; top: 58px; text-align: center;
    font-weight: 700; font-size: 26px; letter-spacing: 1px; color: var(--white);
  }
  .square-ad .tagline {
    position: absolute; left: 0; right: 0; top: 116px; text-align: center;
    font-weight: 600; font-size: 31px; color: var(--white); letter-spacing: -0.5px;
  }
  .square-ad .offer {
    position: absolute; left: 0; right: 0; top: 160px; text-align: center;
    font-weight: 500; font-size: 19px; color: var(--white);
  }
  .square-ad .cta {
    position: absolute; left: 0; right: 0; top: 228px; text-align: center;
    font-weight: 500; font-size: 26px; color: var(--white);
  }
  .square-ad .partner-badge { left: 8px; top: 436px; width: 76px; height: 58px; }
</style>
</head>
<body>

<section class="banner-ad" aria-label="Banner ad">
  <div class="home-photo" role="img" aria-label="Photo of a white board-and-batten custom garage home with dark doors, trees and blossoms"></div>
  <svg class="panel" viewBox="0 0 800 534" aria-hidden="true">
    <polygon points="44,12 470,12 422,466 44,466" fill="#ffffff"/>
    <polygon points="482,12 496,12 446,466 432,466" fill="#e8141b"/>
    <polygon points="76,268 340,268 310,380 76,380" fill="#e8141b"/>
    <polygon points="300,300 318,300 296,362 278,362" fill="#ffffff"/>
  </svg>
  <div class="brand-name">WHITMORE ASH</div>
  <div class="tagline">FOREVER HOME</div>
  <div class="offer">Price Lock<br>Available!</div>
  <div class="cta">Learn More
    <svg class="cta-icon" viewBox="0 0 34 34" aria-hidden="true">
      <circle cx="17" cy="17" r="14" fill="none" stroke="#e8141b" stroke-width="3"/>
      <polygon points="13,10 24,17 13,24" fill="#e8141b"/>
    </svg>
  </div>
  <div class="partner-badge" aria-label="QVTG member badge"></div>
</section>

<section class="square-ad" aria-label="Square ad">
  <div class="home-photo" role="img" aria-label="Photo of a white farmhouse-style custom home with a red barn-style garage and trees"></div>
  <svg class="bands" viewBox="0 0 500 500" aria-hidden="true">
    <polygon points="0,0 500,0 500,116 250,206 0,146" fill="#3b3e43"/>
    <polygon points="0,146 250,206 500,116 500,196 250,296 0,216" fill="#e8141b"/>
  </svg>
  <div class="brand-name">WHITMORE ASH</div>
  <div class="tagline">FOREVER HOME</div>
  <div class="offer">Price Lock Available!</div>
  <div class="cta">Learn More</div>
  <div class="partner-badge" aria-label="QVTG member badge"></div>
</section>

</body>
</html>
```